BRIGHTWELL PROPERTY CHECKS Business card, please make it match the flyer.
Dana Pelworth
Dana@brightwellpropertychecksfl.example
555-218-7604 office
www.BrightwellPropertyChecks.example

Contact Information for Business Card

OUR LOGO

```html
<!DOCTYPE html>
<html lang="en">
<head>
<meta charset="utf-8">
<title>Brightwell Property Checks – Business Card</title>
<link rel="stylesheet" href="https://fonts.googleapis.com/css2?family=Lato:wght@400;700;900&display=swap">
<style>
  :root {
    --stage: #2b2d31;
    --card-blue: #1565c8;
    --card-blue-deep: #0f57b3;
    --flag-red: #e4202a;
    --ink-white: #ffffff;
    --faint-blue: rgba(10, 60, 150, 0.35);
  }
  * { box-sizing: border-box; margin: 0; padding: 0; }
  html, body {
    width: 1200px; height: 952px; overflow: hidden;
    background: var(--stage);
    font-family: "Lato", sans-serif;
  }
  .canvas {
    position: relative; width: 1200px; height: 952px;
  }
  .card {
    position: absolute; left: 250px; width: 700px; height: 400px;
    border-radius: 22px; overflow: hidden;
    background: linear-gradient(160deg, var(--card-blue) 0%, var(--card-blue-deep) 100%);
    box-shadow: 0 14px 30px rgba(0,0,0,0.45);
  }
  .card--back { top: 40px; }
  .card--front { top: 512px; }

  .brand {
    position: absolute; display: flex; align-items: center; gap: 12px;
    color: var(--ink-white); font-weight: 900; letter-spacing: 0.04em;
  }
  .brand__dot {
    flex: none; border-radius: 50%; background: var(--flag-red);
  }
  .brand__name { line-height: 1.1; }

  .card--back .brand { left: 110px; top: 48px; width: 280px; }
  .card--back .brand__dot { width: 56px; height: 56px; }
  .card--back .brand__name { font-size: 22px; }

  .brand-watermark {
    position: absolute; right: 30px; bottom: 26px;
    color: var(--faint-blue); font-weight: 900; font-size: 40px;
    line-height: 1.05; text-align: right; letter-spacing: 0.04em;
  }

  .contacts {
    position: absolute; left: 48px; top: 178px; list-style: none;
    color: var(--ink-white); font-size: 17px;
  }
  .contacts li { display: flex; align-items: center; gap: 10px; margin-bottom: 10px; }
  .contacts .icon {
    width: 22px; height: 22px; border-radius: 4px; background: var(--flag-red);
    display: flex; align-items: center; justify-content: center; flex: none;
  }

  .person {
    position: absolute; right: 48px; top: 170px; text-align: right;
  }
  .person__name {
    font-size: 36px; font-weight: 700; letter-spacing: 0.02em;
    text-transform: uppercase; color: var(--ink-white);
  }
  .person__name .surname { color: var(--flag-red); }
  .person__title {
    font-size: 20px; color: var(--ink-white); margin-top: 4px;
    padding-bottom: 6px; border-bottom: 2px solid var(--ink-white);
    display: inline-block;
  }

  .front-band { position: absolute; inset: 0; }
  .card--front .brand {
    left: 50%; top: 70px; transform: translateX(-50%); width: 430px;
  }
  .card--front .brand__dot { width: 70px; height: 70px; }
  .card--front .brand__name { font-size: 30px; }
</style>
</head>
<body>
<main class="canvas">

  <section class="card card--back" aria-label="Business card, contact side">
    <div class="brand-watermark" aria-hidden="true">BRIGHTWELL<br>PROPERTY CHECKS</div>

    <div class="brand">
      <span class="brand__dot"></span>
      <span class="brand__name">BRIGHTWELL PROPERTY CHECKS</span>
    </div>

    <ul class="contacts">
      <li>
        <span class="icon">
          <svg width="14" height="14" viewBox="0 0 24 24" aria-hidden="true"><path fill="#fff" d="M6.6 10.8a15 15 0 0 0 6.6 6.6l2.2-2.2c.3-.3.7-.4 1-.2 1.1.4 2.3.6 3.6.6.6 0 1 .4 1 1V20c0 .6-.4 1-1 1A17 17 0 0 1 3 4c0-.6.4-1 1-1h3.5c.6 0 1 .4 1 1 0 1.3.2 2.5.6 3.6.1.3 0 .7-.2 1z"/></svg>
        </span>
        555-218-7604 office
      </li>
      <li>
        <span class="icon">
          <svg width="14" height="14" viewBox="0 0 24 24" aria-hidden="true"><path fill="#fff" d="M3 5h18v14H3z"/><path fill="none" stroke="#e4202a" stroke-width="2" d="M3 5l9 8 9-8"/></svg>
        </span>
        Dana@brightwellpropertychecksfl.example
      </li>
      <li>
        <span class="icon">
          <svg width="14" height="14" viewBox="0 0 24 24" aria-hidden="true"><path fill="#fff" d="M4 20L12 3l8 17-8-5z"/></svg>
        </span>
        www.BrightwellPropertyChecks.example
      </li>
    </ul>

    <div class="person">
      <div class="person__name">Dana <span class="surname">Pelworth</span></div>
      <div class="person__title">Managing Director</div>
    </div>
  </section>

  <section class="card card--front" aria-label="Business card, logo side">
    <svg class="front-band" width="700" height="400" viewBox="0 0 700 400" aria-hidden="true">
      <path fill="#e4202a" d="M0 250 C 160 270, 260 300, 380 330 S 600 360, 700 250 L 700 400 L 0 400 Z"/>
      <path fill="#1565c8" d="M0 240 C 160 262, 260 292, 380 322 S 600 352, 700 242 L 700 250 C 600 360, 500 340, 380 330 S 160 270, 0 250 Z" opacity="0.9"/>
    </svg>
    <div class="brand">
      <span class="brand__dot"></span>
      <span class="brand__name">BRIGHTWELL PROPERTY CHECKS</span>
    </div>
  </section>

</main>
</body>
</html>
```